Harrowgate Supply Group Business Card Design

The Business Card will be one side only with Harrowgate Supplies Group Logo
Card should have:
Name
Title
Office phone Number
Cell Number
email address
Website
Street Address
Our Slogan is Rugged and Reliable
Looking for something that stands out from other business cards

Target Market(s)

Heavy equipment Lease Company

```html
<!DOCTYPE html>
<html lang="en">
<head>
<meta charset="UTF-8">
<title>Harrowgate Supplies Group – Business Card</title>
<link rel="stylesheet" href="https://fonts.googleapis.com/css2?family=Open+Sans:wght@400;600;700&display=swap">
<style>
  :root {
    --backdrop: #2b2f36;
    --card: #1d1a1b;
    --pattern-dark: #262223;
    --pattern-light: #2f2a2b;
    --text-muted: #b9b6b6;
    --text-bright: #f4f2f2;
    --brand-red: #c8202f;
    --brand-blue: #2a2f8f;
  }
  * { box-sizing: border-box; margin: 0; padding: 0; }
  html, body {
    width: 1200px;
    height: 900px;
    overflow: hidden;
    background: var(--backdrop);
    font-family: "Open Sans", Arial, sans-serif;
  }
  .business-card {
    position: absolute;
    left: 100px;
    top: 164px;
    width: 1000px;
    height: 572px;
    background: var(--card);
    overflow: hidden;
    box-shadow: 0 18px 40px rgba(0,0,0,0.45);
  }
  .star-field {
    position: absolute;
    inset: 0;
    width: 100%;
    height: 100%;
  }
  .brand-mark {
    position: absolute;
    left: 58px;
    top: 42px;
    display: flex;
    align-items: center;
    gap: 12px;
  }
  .brand-mark__square {
    width: 22px;
    height: 22px;
    background: var(--brand-blue);
  }
  .brand-mark__name {
    font-size: 22px;
    font-weight: 700;
    color: var(--brand-red);
    letter-spacing: 0.5px;
    text-transform: uppercase;
  }
  .contact-block {
    position: absolute;
    left: 120px;
    top: 112px;
    color: var(--text-muted);
  }
  .contact-block__name {
    font-size: 34px;
    font-weight: 400;
    line-height: 1.1;
  }
  .contact-block__title {
    font-size: 22px;
    margin-top: 2px;
    margin-bottom: 34px;
  }
  .contact-block__line {
    font-size: 20px;
    line-height: 1.65;
  }
  .slogan {
    position: absolute;
    right: 84px;
    top: 352px;
    font-size: 38px;
    font-weight: 700;
    color: var(--text-bright);
    letter-spacing: 2px;
  }
  .website {
    position: absolute;
    left: 470px;
    top: 488px;
    font-size: 19px;
    font-weight: 600;
    color: var(--text-bright);
    letter-spacing: 8px;
  }
</style>
</head>
<body>
  <div class="business-card">
    <svg class="star-field" viewBox="0 0 1000 572" role="img" aria-label="Faint tonal star pattern decoration">
      <defs>
        <linearGradient id="starFieldTone" x1="0" y1="0" x2="1" y2="1">
          <stop offset="0" stop-color="#262223"/>
          <stop offset="1" stop-color="#2f2a2b"/>
        </linearGradient>
      </defs>
      <polygon points="640,110 1000,60 1000,572 330,572 390,330" fill="url(#starFieldTone)"/>
    </svg>

    <div class="brand-mark">
      <span class="brand-mark__square"></span>
      <span class="brand-mark__name">Harrowgate Supplies Group</span>
    </div>

    <div class="contact-block">
      <p class="contact-block__name">Your Name</p>
      <p class="contact-block__title">Title</p>
      <p class="contact-block__line">999 999 9999</p>
      <p class="contact-block__line">999 999 9999</p>
      <p class="contact-block__line">email@website.com</p>
      <p class="contact-block__line">Street Address</p>
    </div>

    <p class="slogan">Rugged and Reliable</p>
    <p class="website">www.website.com</p>
  </div>
</body>
</html>
```